Peptide Weight Loss Trifold

A trifold to market peptide weight loss injections. We are different than other clinics, in that we offer a three step approach to effortlessly lose weight and keep it off.

The peptides used are Veltrazine and KRX5120, both proven to . We also have Corvina Balance, a product that heals the gut biome and brain hormone response to weight loss. These three items stacked together is what sets us apart from other clinics. Both peptides are approved by the FDA for weight loss.

We also compound our peptides so they are much cheaper than the commercial Veltrazine also known as Lunaxor, and Trelima. These two commercial peptides from big pharma, each run about 1200.00 per month. Our compounded peptides are a fraction of that cost.
KRX5120....(Anti Obesity Drug)
Patients are losing as much weight as if they had bariatric surgery. 3-5 pounds per week.

If your are like 85% of dieters, its not your first time trying to get healthy and lose weight.
Join thousands of folks pushing the past plateaus and kill the cravings without starving via Halcrest MD's 16-Week program.
Five Star reviews.
"I have been on Veltrazine for one month. I guess the numbers are the crucial part of all veltrazine reviews. That’s it. I have dropped 16lbs. One of the things I have truly come to appreciate is that Vel will limit your appetite. " Maren
"I’ve lost 13.5 pounds in a month, and I can’t even tell how it happened. The interesting part is that I don’t want to eat sweets anymore. I just want to eat less, I eat small portions while losing weight and enjoy my life." Tilda84
" I’ve been on the double peptide plan for a month and have dropped 20 pounds, despite not exercising. I’m delighted to see these figures change." Quinby
"Veltrazine worked for me. 10 out of 10." Ned

Hunger pangs! The primary roadblock to weight loss. With veltrazine, hunger pangs are a thing of the past. Veltrazine....changing the game!

Benefits of Veltrazine:
Reduces hunger pangs
Makes you feel fuller longer
Reduces food cravings
Reduces cardiovascular risk factors
Improves insulin sensitivity
Convenient once-weekly dosing

Is Veltrazine Safe?
Veltrazine is a safe, FDA-approved medication with minimal side effects.

Benefits of KRX 5120
Fat doesn’t stand a chance against this naturally powerful peptide, whose impressive fat-fighting abilities can provide the following benefits, such as:

Reduces body fat
Increases calorie burn
Triggers fat release>
Boosts your metabolism
Prevents non-fatty foods from turning into body fat
Doesn’t increase your appetite

A weight loss breakthrough.
Recent scientific discoveries offer insight into how our metabolism and hormones change over time — and how that impacts whether we’ll gain or lose weight. It comes down to the relationship between our brains and our guts.

A new family of medications called GLP-1s address these biological factors head-on. THE TRUTH IS...
It's not about willpower.
It's biology.
Up to 70% of weight gain is linked to genetics. On top of that, other health conditions and medications can make weight loss even more difficult.

And the environment we live in can influence our access to affordable and reliable healthcare and nutrition.

Peptide GLP-1s fight back against these genetic, biological, and environmental factors that prevent weight loss.
244 genes linked to obesity
BOOSTING YOUR BODY'S NATURAL ABILITIES
How GLP-1s Work
WHAT

A naturally occurring hormone
GLP-1 is naturally released by the gut in response to food.

HOW

An extra boost for your system
The effects include increasing insulin release from the pancreas, slowing down stomach emptying, and targeting receptors in the brain that cause appetite reduction.

RESULT

A more efficient weight loss outcome
This results in a sensation of satiety, or fullness, lasting much longer than possible with natural GLP-1 hormone levels.
Other medications
Your Pathwell Clinician may determine that another medication or a combination of medications might work best for your medical history and biology. They will do a careful review of your specific case to ensure you’re getting an effective medication that meets your needs.

You can learn more about different medications, common side effects, and their results and costs, by call us today for a free consultation at 555-318-SLIM

Here is a layout that I woukd like inside on the bottom half

Went on vacation/holiday

Target Market(s)

anyone with a BMI over28

Industry/Entity Type

medical weight loss

Requirements
Must have
• call to action
Nice to have
• include 5 star review
Should not have
• too many words

```html
<!DOCTYPE html>
<html lang="en">
<head>
<meta charset="utf-8">
<title>Halcrest MD – Peptide Weight Loss Trifold</title>
<link href="https://fonts.googleapis.com/css2?family=Montserrat:wght@400;500;600;700;800&family=Oswald:wght@500&display=swap" rel="stylesheet">
<style>
:root{
  --lime:#8dc63f;
  --green:#62a02e;
  --deep-green:#4d7f22;
  --ink:#231f20;
  --grey:#6d6e71;
  --light-grey:#e6e7e8;
  --panel-dark:#2b2b2b;
  --card-dark:#1f1f1f;
  --white:#ffffff;
  --stage:#f1f1f1;
}
*{box-sizing:border-box;margin:0;padding:0}
html,body{width:1200px;height:2400px;overflow:hidden}
body{background:var(--stage);font-family:"Montserrat",sans-serif;color:var(--ink);position:relative}
.spread{position:absolute;left:40px;width:1120px;height:792px;background:var(--white);overflow:hidden;box-shadow:0 6px 24px rgba(0,0,0,.12)}
.spread--outside{top:358px}
.spread--inside{top:1250px}
.abs{position:absolute}
.shapes{position:absolute;left:0;top:0;width:1120px;height:792px}
.photo{position:absolute}

/* reviews */
.reviews-title{left:24px;top:22px;font-size:22px;font-weight:600;color:var(--ink)}
.reviews-title span{color:var(--green)}
.review{position:absolute;left:22px;width:328px;background:var(--card-dark);border-radius:8px;padding:12px 12px 10px;color:#fff}
.review .stars{color:#ffd21f;font-size:11px;letter-spacing:1px}
.review p{font-size:10.2px;line-height:1.28;margin-top:4px}
.review .author{color:var(--lime);font-size:10.5px;font-weight:600;margin-top:5px}
.review .quote-mark{position:absolute;left:8px;top:-14px;font-size:34px;font-weight:800;color:var(--lime);line-height:1}

/* brand */
.brand{display:flex;align-items:center;justify-content:center;gap:8px}
.brand .dot{width:14px;height:14px;border-radius:50%;background:var(--lime)}
.brand .name{font-weight:500;color:var(--deep-green)}

.about{left:420px;top:40px;width:280px;text-align:center}
.about .brand .name{font-size:26px}
.about p{font-size:10.2px;line-height:1.3;color:var(--ink);margin-top:20px}

.contact{left:400px;top:478px;width:320px;text-align:center}
.contact h2{font-size:32px;font-weight:600;color:var(--green)}
.contact h2 span{color:var(--ink)}
.contact .icon{display:block;margin:8px auto 2px;width:24px;height:24px}
.contact .line{font-size:14.5px;font-weight:500;line-height:1.2}
.contact .web{font-weight:700;font-size:14px}

.cover-photo{left:1000px;top:270px;width:120px;height:522px;background:linear-gradient(180deg,#efe9e4,#bdb8b4 45%,#3a3a3a 80%,#2a2a2a)}
.cover-brand{left:760px;top:70px;width:340px}
.cover-brand .name{font-size:36px}
.cover-headline{left:770px;top:182px;width:230px}
.cover-headline .lead{font-size:21px;color:var(--grey);font-weight:400}
.cover-headline .big{font-size:32px;font-weight:700;color:var(--grey);line-height:1.3}
.cover-headline .lose{font-size:44px;font-weight:800;color:var(--lime);line-height:1.1}
.cover-headline .weight{font-size:44px;font-weight:800;color:var(--deep-green);line-height:1.1}
.cover-product{left:772px;top:630px;width:215px}
.cover-product h3{font-size:22px;font-weight:700;color:var(--green)}
.cover-product p{font-size:11.8px;font-weight:500;line-height:1.25;color:var(--ink)}
.web-button{left:788px;top:737px;width:284px;height:30px;background:var(--green);border-radius:4px;color:#fff;font-size:13px;font-weight:700;letter-spacing:3px;text-align:center;line-height:30px}

/* inside */
.peptides{left:24px;top:22px;width:322px}
.peptides .kicker{font-size:15px;font-weight:600;color:var(--lime)}
.peptides h3{font-size:15.5px;font-weight:600}
.peptides p{font-size:10.8px;line-height:1.28;margin-top:2px}
.compound{left:24px;top:165px;width:330px}
.compound h3{font-size:16px;font-weight:600;line-height:1.18}
.compound h3 em{font-style:normal;color:var(--lime)}
.compound .small{font-size:10px;color:var(--ink);margin-top:16px}
.price-bar{display:flex;margin-top:6px;font-size:10px;font-weight:700;letter-spacing:1px;color:#fff}
.price-bar span{padding:2px 10px}
.price-bar .k{background:var(--panel-dark)}
.price-bar .v{background:var(--lime)}
.compound .note{font-size:10px;margin-top:4px;line-height:1.25}
.results{left:24px;top:355px;width:330px;display:flex;align-items:center;gap:10px}
.results p{font-size:11.6px;font-weight:600;line-height:1.25;width:165px}
.results .rule{width:2px;height:46px;background:var(--ink)}
.results .figure{font-family:"Oswald",sans-serif;font-size:27px;line-height:1.05;color:var(--lime)}
.results .figure b{color:var(--ink);font-weight:500;display:block}

.dark-panel{left:373px;top:0;width:374px;height:792px;background:var(--panel-dark)}
.hunger{left:395px;top:18px;width:330px;color:#fff}
.hunger h2{font-size:30px;font-weight:700;color:var(--lime)}
.hunger p{font-size:10.6px;font-weight:600;line-height:1.25;margin-top:4px}
.hunger .game{font-size:14.5px;font-weight:600;line-height:1.25;margin-top:2px}
.hunger h3{font-size:18px;font-weight:600;color:var(--lime);margin-top:14px}
.hunger .safe{font-size:10.5px;font-weight:400;margin-top:4px}
.benefit-head{left:395px;top:265px;color:#fff}
.benefit-head .k{font-size:17px;font-weight:600;color:var(--lime);line-height:1}
.benefit-head .t{font-size:17px;font-weight:600;line-height:1.2}
.benefit-grid{left:388px;top:288px;width:340px;height:190px;border:1px dashed rgba(141,198,63,.55);border-left:none;border-bottom:none;display:grid;grid-template-columns:repeat(3,1fr);grid-template-rows:repeat(2,1fr);padding-top:12px}
.benefit{text-align:center;color:#fff;font-size:10.5px;font-weight:600;line-height:1.2}
.benefit svg{display:block;margin:0 auto 6px;width:34px;height:34px}
.dieters{left:395px;top:496px;width:180px;color:#fff;font-size:15px;font-weight:600;line-height:1.22}
.dieters b{color:var(--lime);font-size:20px;font-weight:700}
.program{left:560px;top:622px;width:220px;color:#fff}
.program p{font-size:11.5px;font-weight:600;line-height:1.2;font-style:italic}
.program h3{font-family:"Oswald",sans-serif;font-size:25px;font-weight:500;line-height:1.12;margin-top:8px}

.krx{left:770px;top:22px;width:330px}
.krx .k{font-size:17px;font-weight:600;color:var(--lime);line-height:1}
.krx h3{font-size:17px;font-weight:600}
.krx p{font-size:11.8px;line-height:1.25;margin-top:6px}
.ticks{left:770px;top:160px;width:330px;display:grid;grid-template-columns:150px 170px;column-gap:16px}
.ticks ul{list-style:none}
.ticks li{display:flex;gap:7px;font-size:12px;font-weight:600;line-height:1.2;margin-bottom:15px}
.ticks li svg{flex:none;width:12px;height:12px;margin-top:2px}
</style>
</head>
<body>

<section class="spread spread--outside" aria-label="Trifold outside">
  <svg class="shapes" viewBox="0 0 1120 792" aria-hidden="true">
    <defs>
      <linearGradient id="lowerGrey" x1="0" y1="0" x2="0" y2="1">
        <stop offset="0" stop-color="#f4f4f4"/><stop offset="1" stop-color="#e8e8e8"/>
      </linearGradient>
    </defs>
    <path d="M0 500 C220 430 500 400 760 410 C950 418 1050 400 1120 360 L1120 792 L0 792Z" fill="url(#lowerGrey)"/>
    <path d="M0 520 C220 430 500 392 760 398 C950 402 1050 372 1120 320 L1120 345 C1050 410 950 440 760 438 C500 436 260 470 0 570Z" fill="var(--lime)"/>
    <path d="M0 560 C120 520 240 500 330 500 L330 792 L0 792Z" fill="var(--green)" opacity=".85"/>
    <path d="M880 0 C1010 20 1090 70 1120 130 L1120 0Z" fill="var(--lime)"/>
    <path d="M900 0 C1010 30 1080 90 1095 150 C1110 230 1080 330 980 400 L1120 390 L1120 0Z" fill="none" stroke="var(--lime)" stroke-width="3" opacity=".6"/>
  </svg>

  <h2 class="abs reviews-title"><span>Our</span> Reviews...</h2>
  <div class="review" style="top:72px;height:112px">
    <span class="quote-mark">“</span>
    <div class="stars">★★★★★</div>
    <p>I’ve lost 13.5 pounds in a month, and I can’t even tell how it happened. The interesting part is that I don’t want to eat sweets anymore. I just want to eat less, I eat small portions while losing weight and enjoy my life.</p>
    <div class="author">-Tilda84</div>
  </div>
  <div class="review" style="top:212px;height:102px">
    <span class="quote-mark">“</span>
    <div class="stars">★★★★★</div>
    <p>I’ve been on the double peptide plan for a month and have dropped 20 pounds, despite not exercising. I’m delighted to see these figures change.</p>
    <div class="author">-Quinby</div>
  </div>
  <div class="review" style="top:342px;height:74px;left:20px">
    <span class="quote-mark">“</span>
    <div class="stars">★★★★★</div>
    <p>Veltrazine worked for me. 10 out of 10</p>
    <div class="author">-Ned</div>
  </div>

  <div class="photo" role="img" aria-label="Photo of a clinician measuring a smiling patient's waist with a tape measure" style="left:30px;top:490px;width:300px;height:302px;background:linear-gradient(135deg,#c9d7b2,#eeeeee 60%,#f7f7f7)"></div>

  <div class="abs about">
    <div class="brand"><span class="dot"></span><span class="name">Halcrest MD</span></div>
    <p>Halcrest MD has built a team of collaborative experts that are dedicated to serving the well-being of their clients. Our mission is to address the whole person by integrating different modalities in a safe, effective, supportive environment. Our team brings together the latest weight loss technology with sound nutrition, exercise, and education that can change your life forever. Each of our skilled practitioners has years of experience in helping people just like you achieve their weight loss goals. We look forward to the opportunity to partner with you in seeing your dreams become reality.</p>
  </div>
  <div class="photo" role="img" aria-label="Photo of an alarm clock, green dumbbells and a tape measure" style="left:430px;top:300px;width:290px;height:150px;background:linear-gradient(90deg,#d9d9d9,#a5d46a 60%,#7dbb35)"></div>

  <div class="abs contact">
    <h2>Contact <span>Us</span></h2>
    <svg class="icon" viewBox="0 0 24 24"><circle cx="12" cy="12" r="12" fill="var(--ink)"/><path d="M12 5a4 4 0 0 0-4 4c0 3 4 8 4 8s4-5 4-8a4 4 0 0 0-4-4zm0 5.5A1.5 1.5 0 1 1 12 7.5a1.5 1.5 0 0 1 0 3z" fill="var(--lime)"/></svg>
    <div class="line">Ridgeview Office<br>4820 W Cedar Mesa Suite #B210<br>Ridgeview Arizona 85099</div>
    <svg class="icon" viewBox="0 0 24 24"><circle cx="12" cy="12" r="12" fill="var(--ink)"/><path d="M8.5 6.5l2 2-1.2 1.6c.8 1.6 2 2.8 3.6 3.6l1.6-1.2 2 2-1.3 1.8c-4-.6-7.7-4.3-8.3-8.3z" fill="var(--lime)"/></svg>
    <div class="line">(555) 318-7546</div>
    <svg class="icon" viewBox="0 0 24 24"><circle cx="12" cy="12" r="12" fill="var(--ink)"/><rect x="7" y="10" width="10" height="6" rx="1" fill="var(--lime)"/><rect x="9" y="6" width="6" height="4" fill="var(--lime)"/></svg>
    <div class="line">(555) 318-7547</div>
    <svg class="icon" viewBox="0 0 24 24"><circle cx="12" cy="12" r="12" fill="var(--ink)"/><circle cx="12" cy="12" r="6" fill="none" stroke="var(--lime)" stroke-width="1.5"/><path d="M6 12h12M12 6c-2 2-2 10 0 12M12 6c2 2 2 10 0 12" fill="none" stroke="var(--lime)" stroke-width="1.2"/></svg>
    <div class="line web">www.HalcrestMD.com</div>
  </div>

  <div class="photo cover-photo" role="img" aria-label="Photo of a fit young woman in sportswear holding a tape measure around her waist"></div>
  <div class="abs brand cover-brand"><span class="dot"></span><span class="name">Halcrest MD</span></div>
  <div class="abs cover-headline">
    <div class="lead">A three step</div>
    <div class="big">Approach to<br>Effortlessly</div>
    <div class="lose">Lose</div>
    <div class="weight">Weight</div>
  </div>
  <div class="abs cover-product">
    <h3>Veltrazine</h3>
    <p>Introducing the new FDA<br>Approved Treatment for<br>Weight Management</p>
  </div>
  <div class="abs web-button">www.HalcrestMD.com</div>
</section>

<section class="spread spread--inside" aria-label="Trifold inside">
  <div class="abs dark-panel"></div>
  <svg class="shapes" viewBox="0 0 1120 792" aria-hidden="true">
    <defs>
      <linearGradient id="greenGlow" x1="0" y1="1" x2="1" y2="0">
        <stop offset="0" stop-color="#4f8a1f"/><stop offset=".6" stop-color="#8dc63f"/><stop offset="1" stop-color="#b8dc84"/>
      </linearGradient>
    </defs>
    <path d="M540 792 C590 600 760 470 1120 440 L1120 792Z" fill="url(#greenGlow)"/>
    <path d="M520 792 C570 590 750 455 1120 425" fill="none" stroke="var(--lime)" stroke-width="6"/>
    <path d="M0 700 C200 720 300 760 373 792 L0 792Z" fill="var(--lime)" opacity=".9"/>
  </svg>

  <div class="abs peptides">
    <div class="kicker">The peptides used are</div>
    <h3>Veltrazine and KRX5120,</h3>
    <p>both proven to . We also have Corvina Balance, a product that heals the gut biome and brain hormone response to weight loss. These three items stacked together is what sets us apart from other clinics. Both peptides are approved by the FDA for weight loss.</p>
  </div>
  <div class="abs compound">
    <h3>We also compound our peptides so they are much cheaper than the commercial <em>Veltrazine also known as Lunaxor, and Trelima.</em></h3>
    <p class="small">These two commercial peptides from big pharma.</p>
    <div class="price-bar"><span class="k">EACH RUN ABOUT</span><span class="v">1200.00 PER MONTH</span></div>
    <p class="note">Our compounded peptides are a fraction of that cost.<br>KRX5120....(Anti Obesity Drug)</p>
  </div>
  <div class="abs results">
    <p>Patients are losing as much weight as if they had bariatric surgery</p>
    <span class="rule"></span>
    <div class="figure">3-5 POUNDS<b>PER WEEK</b></div>
  </div>
  <div class="photo" role="img" aria-label="Photo of a happy couple holding out oversized jeans after weight loss" style="left:120px;top:430px;width:250px;height:362px;background:linear-gradient(180deg,#f2f2f2,#c8b9b0 50%,#8b3a3e)"></div>

  <div class="abs hunger">
    <h2>Hunger pangs!</h2>
    <p>The primary roadblock to<br>weight loss. With veltrazine,<br>hunger pangs are a thing of the past.</p>
    <div class="game">Veltrazine....<br>changing the game!</div>
    <h3>Is Veltrazine Safe?</h3>
    <p class="safe">Veltrazine is a safe, FDA-approved medication with minimal side effects.</p>
  </div>
  <div class="abs benefit-head"><div class="k">BENEFITS</div><div class="t">OF VELTRAZINE</div></div>
  <div class="abs benefit-grid">
    <div class="benefit"><svg viewBox="0 0 34 34"><circle cx="17" cy="17" r="15" fill="none" stroke="var(--lime)" stroke-width="1.5"/><circle cx="17" cy="17" r="7" fill="none" stroke="#fff" stroke-width="1.5"/><path d="M11 23L23 11" stroke="#fff" stroke-width="1.5"/></svg>Reduces<br>hunger pangs</div>
    <div class="benefit"><svg viewBox="0 0 34 34"><circle cx="17" cy="17" r="15" fill="none" stroke="var(--lime)" stroke-width="1.5"/><path d="M12 10v14M22 10v14M12 17h10" stroke="#fff" stroke-width="1.5"/></svg>Makes you<br>feel fuller<br>longer</div>
    <div class="benefit"><svg viewBox="0 0 34 34"><circle cx="17" cy="17" r="15" fill="none" stroke="var(--lime)" stroke-width="1.5"/><circle cx="17" cy="18" r="6" fill="none" stroke="#fff" stroke-width="1.5"/><path d="M17 12c0-3 2-4 3-4" stroke="#fff" stroke-width="1.5" fill="none"/></svg>Reduces<br>food cravings</div>
    <div class="benefit"><svg viewBox="0 0 34 34"><circle cx="17" cy="17" r="15" fill="none" stroke="var(--lime)" stroke-width="1.5"/><path d="M17 24l-6-6a3.5 3.5 0 0 1 6-4a3.5 3.5 0 0 1 6 4z" fill="none" stroke="#fff" stroke-width="1.5"/></svg>Reduces<br>cardiovascular<br>risk factors</div>
    <div class="benefit"><svg viewBox="0 0 34 34"><circle cx="17" cy="17" r="15" fill="none" stroke="var(--lime)" stroke-width="1.5"/><path d="M17 9c-4 6-5 8-5 10a5 5 0 0 0 10 0c0-2-1-4-5-10z" fill="none" stroke="#fff" stroke-width="1.5"/></svg>Improves<br>insulin<br>sensitivity</div>
    <div class="benefit"><svg viewBox="0 0 34 34"><circle cx="17" cy="17" r="15" fill="none" stroke="var(--lime)" stroke-width="1.5"/><rect x="10" y="11" width="14" height="13" rx="1.5" fill="none" stroke="#fff" stroke-width="1.5"/><path d="M10 15h14M14 9v4M20 9v4" stroke="#fff" stroke-width="1.5"/></svg>Convenient<br>once-weekly<br>dosing</div>
  </div>
  <div class="abs dieters">If your are like<br><b>85% of dieters,</b><br>its not your<br>first time trying<br>to get healthy<br>and lose<br>weight.</div>

  <div class="photo" role="img" aria-label="Photo of a slim waist with a weight-loss injection pen held against it" style="left:770px;top:420px;width:350px;height:372px;background:linear-gradient(200deg,#d8c7b8,#c9a98f 45%,#6f8fb4 85%);opacity:.85"></div>

  <div class="abs program">
    <p>Join thousands of folks pushing the past plateaus and kill the cravings without starving via</p>
    <h3>HALCREST MD’S<br>16-WEEK PROGRAM.</h3>
  </div>

  <div class="abs krx">
    <div class="k">BENEFITS</div>
    <h3>OF KRX 5120</h3>
    <p>Fat doesn’t stand a chance against this naturally powerful peptide, whose impressive fat-fighting abilities can provide the following benefits, such as:</p>
  </div>
  <div class="abs ticks">
    <ul>
      <li><svg viewBox="0 0 12 12"><circle cx="6" cy="6" r="6" fill="var(--lime)"/><path d="M3 6l2 2 4-4" stroke="#fff" stroke-width="1.5" fill="none"/></svg>Reduces body fat</li>
      <li><svg viewBox="0 0 12 12"><circle cx="6" cy="6" r="6" fill="var(--lime)"/><path d="M3 6l2 2 4-4" stroke="#fff" stroke-width="1.5" fill="none"/></svg>Increases calorie burn</li>
      <li><svg viewBox="0 0 12 12"><circle cx="6" cy="6" r="6" fill="var(--lime)"/><path d="M3 6l2 2 4-4" stroke="#fff" stroke-width="1.5" fill="none"/></svg>Triggers fat release</li>
      <li><svg viewBox="0 0 12 12"><circle cx="6" cy="6" r="6" fill="var(--lime)"/><path d="M3 6l2 2 4-4" stroke="#fff" stroke-width="1.5" fill="none"/></svg>Boosts your metabolism</li>
    </ul>
    <ul>
      <li><svg viewBox="0 0 12 12"><circle cx="6" cy="6" r="6" fill="var(--lime)"/><path d="M3 6l2 2 4-4" stroke="#fff" stroke-width="1.5" fill="none"/></svg>Prevents non-fatty foods from turning into body fat</li>
      <li><svg viewBox="0 0 12 12"><circle cx="6" cy="6" r="6" fill="var(--lime)"/><path d="M3 6l2 2 4-4" stroke="#fff" stroke-width="1.5" fill="none"/></svg>Doesn’t increase your appetite</li>
    </ul>
  </div>
</section>

</body>
</html>
```